Velto Studio - Lash Serum Packaging

Need Packaging done for this Lash Serum for a brand called "Velto Studio". The bottle will remain black but the box can be any color. This will be for a 3ml bottle. Give me different options for packaging that is minimalist and clean for this brand that makes it look expensive and make people want to buy.

```html
<!DOCTYPE html>
<html lang="en">
<head>
<meta charset="utf-8">
<title>Velto Studio – Lash Serum Carton Dieline</title>
<link href="https://fonts.googleapis.com/css2?family=Montserrat:wght@400;500;600;700&display=swap" rel="stylesheet">
<style>
  :root {
    --board: #332b2a;
    --crease: #3a7d22;
    --crease-bright: #4fd11a;
    --window: #d2d3d5;
    --ink-light: #ecebea;
    --ink-dark: #332b2a;
    --paper: #ffffff;
  }
  html, body { margin: 0; padding: 0; overflow: hidden; background: var(--paper); }
  .canvas { width: 1200px; height: 1183px; display: block; }
  .board { fill: var(--board); }
  .crease { fill: none; stroke: var(--crease); stroke-width: 3; }
  .crease-bright { fill: none; stroke: var(--crease-bright); stroke-width: 4; }
  .label-face { fill: var(--board); }
  .window { fill: var(--window); }
  text { font-family: 'Montserrat', sans-serif; }
  .brand-light { fill: var(--ink-light); font-weight: 500; }
  .brand-dark { fill: var(--ink-dark); font-weight: 500; }
  .title { fill: var(--ink-light); font-weight: 600; font-size: 28px; }
  .volume { fill: var(--ink-light); font-weight: 600; font-size: 20px; }
  .body-copy { fill: var(--ink-light); font-size: 16px; font-weight: 400; }
  .heading { fill: var(--ink-light); font-size: 16px; font-weight: 600; }
  .week-tag { font-size: 14px; font-weight: 700; }
  .week-copy { font-size: 14px; font-weight: 600; }
  .week-copy.on-light { fill: var(--ink-dark); }
  .week-copy.on-dark { fill: var(--ink-light); }
  .badge-label { fill: var(--ink-light); font-size: 10px; font-weight: 600; }
  .badge-disc { fill: var(--window); }
  .maker { fill: var(--ink-light); font-weight: 700; }
  .illustration { fill: #8f8c8b; }
  .illustration.on-light { fill: #4a4342; }
  .icon-stroke { fill: none; stroke: var(--ink-light); stroke-width: 3; }
</style>
</head>
<body>
<svg class="canvas" viewBox="0 0 1920 1890" preserveAspectRatio="none" xmlns="http://www.w3.org/2000/svg">

  <!-- Die-cut board -->
  <path class="board" d="M260,412 L260,140 Q260,55 345,55 L500,55 Q585,55 585,140 L585,255 L780,255 L825,395 L1022,395 L1068,255 L1282,255 L1336,420 L1338,1485 L1282,1660 L1087,1660 L1087,1775 Q1087,1860 1002,1860 L847,1860 Q762,1860 762,1775 L762,1660 L565,1660 L518,1520 L285,1520 L185,1420 L185,480 Z"/>

  <!-- Windows -->
  <rect class="window" x="298" y="432" width="250" height="550"/>
  <rect class="window" x="800" y="432" width="250" height="550"/>

  <!-- Crease lines -->
  <g class="crease">
    <rect x="297" y="432" width="1003" height="1050"/>
    <line x1="548" y1="432" x2="548" y2="1482"/>
    <line x1="798" y1="432" x2="798" y2="1482"/>
    <line x1="1050" y1="432" x2="1050" y2="1482"/>
    <polyline points="297,432 222,497 222,1405 297,1480"/>
    <path d="M297,432 L297,140 Q297,92 345,92 L500,92 Q548,92 548,140 L548,432"/>
    <line x1="297" y1="182" x2="548" y2="182"/>
    <polyline points="548,432 595,292 752,292 798,432"/>
    <polyline points="1050,432 1096,292 1254,292 1300,432"/>
    <polyline points="548,1482 592,1622 750,1622 797,1482"/>
    <polyline points="1050,1482 1096,1622 1254,1622 1300,1482"/>
    <path d="M798,1482 L798,1775 Q798,1822 845,1822 L1003,1822 Q1050,1822 1050,1775 L1050,1482"/>
    <line x1="798" y1="1732" x2="1050" y2="1732"/>
  </g>

  <!-- Panel 1: weekly progress -->
  <g class="progress-panel" text-anchor="middle">
    <rect class="illustration on-light" x="395" y="530" width="55" height="60" rx="4" role="img" aria-label="Single lash strand illustration"/>
    <rect x="390" y="605" width="66" height="22" fill="var(--ink-dark)"/>
    <text class="week-tag" x="423" y="622" fill="var(--window)">WEEK 1</text>
    <text class="week-copy on-light" x="422" y="648">Time to grow, girl! longer</text>
    <text class="week-copy on-light" x="422" y="663">lashes are on the way.</text>

    <rect class="illustration on-light" x="395" y="715" width="60" height="72" rx="4" role="img" aria-label="Lash strands illustration, week two"/>
    <rect x="390" y="808" width="66" height="22" fill="var(--ink-dark)"/>
    <text class="week-tag" x="423" y="825" fill="var(--window)">WEEK 2</text>
    <text class="week-copy on-light" x="422" y="851">Keep going! Consistency</text>
    <text class="week-copy on-light" x="422" y="866">is key.Missing one day is</text>
    <text class="week-copy on-light" x="422" y="881">okey.</text>

    <rect class="illustration" x="388" y="1025" width="72" height="84" rx="4" role="img" aria-label="Lash strands illustration, week three"/>
    <rect x="390" y="1124" width="66" height="22" fill="var(--window)"/>
    <text class="week-tag" x="423" y="1141" fill="var(--ink-dark)">WEEK 3</text>
    <text class="week-copy on-dark" x="422" y="1167">Exciting! You should start</text>
    <text class="week-copy on-dark" x="422" y="1182">Noticing lash growth</text>

    <rect class="illustration" x="384" y="1230" width="82" height="86" rx="4" role="img" aria-label="Full lash strands illustration, week four"/>
    <rect x="390" y="1329" width="66" height="22" fill="var(--window)"/>
    <text class="week-tag" x="423" y="1346" fill="var(--ink-dark)">WEEK 4</text>
    <text class="week-copy on-dark" x="422" y="1372">Here they are! Enjoy your</text>
    <text class="week-copy on-dark" x="422" y="1387">visibly Longer, fuller</text>
    <text class="week-copy on-dark" x="422" y="1402">natural lashes.</text>
  </g>

  <!-- Panel 2: claims + maker -->
  <g class="claims-panel" text-anchor="middle">
    <circle class="badge-disc" cx="673" cy="762" r="37" role="img" aria-label="Cruelty free badge icon"/>
    <text class="badge-label" x="673" y="815">CRUELTY FREE</text>
    <circle class="badge-disc" cx="673" cy="907" r="37" role="img" aria-label="Plant based badge icon"/>
    <text class="badge-label" x="670" y="963">PLANT BASED</text>
    <circle class="badge-disc" cx="673" cy="1057" r="37" role="img" aria-label="Harsh chemical free badge icon"/>
    <text class="badge-label" x="673" y="1109">HARSH CHEMICAL</text>
    <text class="badge-label" x="673" y="1119">FREE</text>
    <circle class="badge-disc" cx="673" cy="1210" r="37" role="img" aria-label="Paraben free badge icon"/>
    <text class="badge-label" x="673" y="1262">PARABEN FREE</text>

    <text class="maker" x="674" y="1378" font-size="14">MANIFACTURED BY:</text>
    <text class="maker" x="672" y="1400" font-size="10">LOREM IPSUM</text>
    <text class="maker" x="672" y="1410" font-size="10">DOLOR SIT ,</text>
    <text class="maker" x="672" y="1420" font-size="10">CONSECTETUER</text>
    <text class="maker" x="672" y="1430" font-size="10">41555 PL S, LOREM</text>
    <text class="maker" x="674" y="1456" font-size="11">WWW.VELTOSTUDIO.COM</text>
  </g>

  <!-- Panel 3: front face -->
  <g class="front-panel" text-anchor="middle">
    <text class="brand-dark" x="925" y="745" font-size="36">Velto Studio</text>
    <text class="title" x="929" y="1219">LASH</text>
    <text class="title" x="929" y="1246">SERUM</text>
    <text class="volume" x="927" y="1437">3ML</text>
  </g>

  <!-- Panel 4: details -->
  <g class="details-panel">
    <text class="brand-light" x="1176" y="520" font-size="30" text-anchor="middle">Velto Studio</text>
    <text class="body-copy" lengthAdjust="spacing">
      <tspan x="1090" y="588" textLength="173">Nourish your lashes the</tspan>
      <tspan x="1090" y="604" textLength="173">way it deserves, with</tspan>
      <tspan x="1090" y="620" textLength="173">natural, rejvenating</tspan>
      <tspan x="1090" y="636" textLength="173">serums, the natural</tspan>
      <tspan x="1090" y="652" textLength="173">approach for fuller and</tspan>
      <tspan x="1090" y="668">thicker eyelshes.</tspan>
    </text>
    <text class="heading" x="1182" y="701" text-anchor="middle">APPLICATION</text>
    <text class="body-copy">
      <tspan x="1090" y="729" textLength="173">Apply directly to the</tspan>
      <tspan x="1090" y="745" textLength="173">skin of the upper</tspan>
      <tspan x="1090" y="761" textLength="173">eyelied at the base of</tspan>
      <tspan x="1090" y="777" textLength="173">the eylashes like</tspan>
      <tspan x="1090" y="793">eyeliner.</tspan>
      <tspan x="1090" y="826">Apply once a day.</tspan>
      <tspan x="1090" y="858" textLength="173">Additional application</tspan>
      <tspan x="1090" y="874" textLength="173">of serum will not</tspan>
      <tspan x="1090" y="890" textLength="173">increase the growth of</tspan>
      <tspan x="1090" y="906">eyelashes.</tspan>
    </text>
    <text class="heading" x="1182" y="938" text-anchor="middle">CAUTION</text>
    <text class="body-copy">
      <tspan x="1090" y="967" textLength="171">Don’t allow the brush</tspan>
      <tspan x="1090" y="983" textLength="171">to contact unhygienic</tspan>
      <tspan x="1090" y="999" textLength="171">object in order to avoid</tspan>
      <tspan x="1090" y="1015" textLength="171">contamination and</tspan>
      <tspan x="1090" y="1031" textLength="171">infections. Avoid direct</tspan>
      <tspan x="1090" y="1047">contact with the eye.</tspan>
      <tspan x="1090" y="1080" textLength="171">Discontinue use if</tspan>
      <tspan x="1090" y="1096" textLength="171">redness or irritaton</tspan>
      <tspan x="1090" y="1112" textLength="171">occurs. If redness or</tspan>
      <tspan x="1090" y="1128" textLength="171">orritation persists or is</tspan>
      <tspan x="1090" y="1144" textLength="171">excessive , consult your</tspan>
      <tspan x="1090" y="1160">physician.</tspan>
    </text>
    <text class="heading" x="1183" y="1198" text-anchor="middle">INGREDIENTS</text>
    <text class="body-copy">
      <tspan x="1094" y="1235">Aqua, glycerinum,</tspan>
      <tspan x="1094" y="1251">Myristicyl,</tspan>
      <tspan x="1094" y="1267">petapeptide-4, sodium</tspan>
      <tspan x="1094" y="1283">hyaluronte, panthenol,</tspan>
      <tspan x="1094" y="1299">acetylterapeptide-3,</tspan>
      <tspan x="1094" y="1315">hexapeptide-3,</tspan>
      <tspan x="1094" y="1331">palmltoyl, tripeptide-1,</tspan>
      <tspan x="1094" y="1347">peg-40, hydrogenated</tspan>
      <tspan x="1094" y="1363">castor oil.</tspan>
    </text>
    <g class="disposal-icons">
      <rect class="icon-stroke" x="1101" y="1404" width="44" height="28" rx="4"/>
      <line class="icon-stroke" x1="1101" y1="1400" x2="1143" y2="1390"/>
      <text x="1123" y="1430" text-anchor="middle" font-size="12" font-weight="700" fill="var(--ink-light)">3M</text>
      <circle class="icon-stroke" cx="1182" cy="1414" r="18" stroke-dasharray="26 12"/>
      <rect class="icon-stroke" x="1220" y="1410" width="18" height="26"/>
      <line class="icon-stroke" x1="1216" y1="1406" x2="1242" y2="1406"/>
      <circle cx="1246" cy="1394" r="5" fill="var(--ink-light)"/>
    </g>
  </g>

  <!-- Tube label -->
  <g class="tube-label">
    <rect class="label-face" x="1503" y="461" width="202" height="1010"/>
    <rect class="crease-bright" x="1503" y="461" width="202" height="1010"/>
    <line class="crease-bright" x1="1503" y1="863" x2="1705" y2="863"/>
    <text class="brand-light" x="1606" y="1095" font-size="24" text-anchor="middle">Velto Studio</text>
    <text class="title" x="1604" y="1327" font-size="24" text-anchor="middle">LASH</text>
    <text class="title" x="1604" y="1351" font-size="24" text-anchor="middle">SERUM</text>
    <text class="volume" x="1602" y="1443" font-size="18" text-anchor="middle">3ML</text>
  </g>
</svg>
</body>
</html>
```